Webdesign für Ingenieurbüro
Zielgruppe
Ingenieurbüro Varnotek GmbH
Leistungen:
Siedlungswasserwirtschaft
Straßen- und Ingenieurbau
Hochwasserschutz / Wasserbau
Pegelanlagen
Komplexerschließungen
Koordinierung nach BaustellV
Landschaftsbau
Zielgruppe ist die Öffentliche Hand
Aufgabenstellung
Leistungsbereiche und Stellenangebote (zZt. 3 Stück) sollen zu gleichen Teilen im Fokus stehen. Call to action zum Berweberformular ist nötig.
Zu beachten wäre, dass das Unternehmen für öffentliche Auftraggeber arbeitet. Die Seite sollte klar strukturiert und seriös wirken.
Der Login-Bereich soll in den Hintergrund treten, eventuell über dem footer.
Logo aus dem Cover - siehe anbei übernehmen

```html
<!DOCTYPE html>
<html lang="de">
<head>
<meta charset="utf-8">
<title>Ingenieurbüro Varnotek GmbH</title>
<link rel="stylesheet" href="https://fonts.googleapis.com/css2?family=Nunito+Sans:wght@300;400;600;700&display=swap">
<style>
  :root {
    --brand-navy: #2b3f94;
    --brand-cyan: #1ba3e0;
    --text: #454b5c;
    --white: #ffffff;
    --sky: #bfd3e0;
    --sky-light: #d3e1ea;
    --facade: #eef1f3;
    --facade-shade: #cfd8de;
  }
  * { box-sizing: border-box; margin: 0; padding: 0; }
  html, body {
    width: 1200px; height: 900px; overflow: hidden;
    background: var(--white);
    font-family: "Nunito Sans", sans-serif;
    color: var(--text);
  }
  .page {
    position: relative; width: 1200px; height: 900px; overflow: hidden;
    background: var(--white);
    border-top: 6px solid var(--brand-navy);
  }
  .hero-visual {
    position: absolute; left: 523px; top: 0; width: 677px; height: 656px;
    background:
      linear-gradient(118deg, rgba(255,255,255,0) 0%, rgba(255,255,255,0) 30%, rgba(244,246,248,.95) 42%, rgba(236,240,243,.95) 62%, rgba(214,222,228,.9) 78%, rgba(236,240,243,.9) 100%),
      linear-gradient(180deg, var(--sky) 0%, var(--sky-light) 55%, var(--facade-shade) 100%);
  }
  .hero-notch {
    position: absolute; left: 523px; top: 201px; width: 68px; height: 309px;
    background: var(--white);
  }
  .brand {
    position: absolute; left: 100px; top: 74px;
    display: flex; align-items: center; gap: 12px;
    font-size: 19px; font-weight: 600; color: var(--brand-navy);
  }
  .brand-mark {
    width: 34px; height: 34px; border-radius: 50%;
    border: 2px solid var(--brand-cyan);
  }
  .main-nav {
    position: absolute; left: 669px; top: 56px;
    display: flex; gap: 14px;
    font-size: 13.5px; color: #3a4150;
  }
  .main-nav a { color: inherit; text-decoration: none; }
  .hero-title {
    position: absolute; left: 100px; top: 239px; width: 420px;
    font-size: 29px; font-weight: 300; line-height: 33px;
    color: var(--brand-cyan);
  }
  .hero-lead {
    position: absolute; left: 100px; top: 314px; width: 370px;
    font-size: 14px; line-height: 25px;
  }
  .hero-actions {
    position: absolute; left: 100px; top: 444px;
    display: flex; gap: 13px;
  }
  .btn {
    height: 36px; padding: 0 13px;
    display: inline-flex; align-items: center;
    font-family: inherit; font-size: 13.5px; font-weight: 600;
    text-decoration: none; border: 1px solid var(--brand-navy);
  }
  .btn-primary { background: var(--brand-navy); color: var(--white); box-shadow: 0 4px 10px rgba(43,63,148,.25); }
  .btn-secondary { background: var(--white); color: var(--brand-navy); }
  .deco-arc { position: absolute; left: 0; top: 0; pointer-events: none; }
  .about-accent {
    position: absolute; left: 92px; top: 794px; width: 8px; height: 106px;
    border-left: 2px solid var(--brand-cyan); border-top: 2px solid var(--brand-cyan);
  }
  .about-photo {
    position: absolute; left: 100px; top: 783px; width: 406px; height: 117px;
    background: linear-gradient(180deg, #c9dcec 0%, #e4ebf3 40%, #b9c2cc 100%);
  }
  .about-text { position: absolute; left: 610px; top: 810px; width: 465px; }
  .about-kicker { font-size: 14px; font-weight: 600; color: var(--brand-cyan); line-height: 18px; }
  .about-title { margin-top: 4px; font-size: 19.5px; font-weight: 600; color: var(--brand-cyan); line-height: 24px; }
  .about-body { margin-top: 12px; font-size: 12.5px; line-height: 22px; }
</style>
</head>
<body>
<div class="page">
  <svg class="deco-arc" width="1200" height="900" aria-hidden="true">
    <path d="M 420 540 A 420 420 0 0 1 410 800" fill="none" stroke="#eceef5" stroke-width="1"/>
  </svg>

  <div class="hero-visual" role="img" aria-label="Foto: moderne weiße Gebäudefassade vor hellblauem Himmel"></div>
  <div class="hero-notch"></div>

  <div class="brand"><span class="brand-mark"></span>Ingenieurbüro Varnotek GmbH</div>

  <nav class="main-nav">
    <a href="#">Home</a><a href="#">Leistungen</a><a href="#">Projekte</a><a href="#">Stellenangebote</a><a href="#">Zertifikate</a><a href="#">Kontakt</a>
  </nav>

  <h1 class="hero-title">Willkommen beim<br>Ingenieurbüro Varnotek</h1>
  <p class="hero-lead">Ihr zuverlässiger Partner für fachgerechte Beratung, Planung und Bauüberwachung von Maßnahmen des Tief-, Wasser- und Straßenbaues.</p>

  <div class="hero-actions">
    <a class="btn btn-primary" href="#">Unsere Leistungen</a>
    <a class="btn btn-secondary" href="#">Offene Stellen</a>
  </div>

  <div class="about-accent"></div>
  <div class="about-photo" role="img" aria-label="Foto: Bürogebäude des Ingenieurbüros mit Parkplatz"></div>

  <section class="about-text">
    <p class="about-kicker">Ingenieurleistungen aus Altenau-Rabenfeld seit 1991</p>
    <h2 class="about-title">Über 25 Jahre Ingenieurbüro Varnotek GmbH</h2>
    <p class="about-body">Willkommen bei der Ingenieurbüro Varnotek GmbH, einem<br>mittelständischen Unternehmen, welches 1991 gegründet wurde.<br>Wir sind ein zuverlässiger Partner für fachgerechte Beratung, Planung und Bauüberwachung von Maßnahmen des Tief-, Wasser- und Straßenbaues.</p>
  </section>
</div>
</body>
</html>
```